Label template request for Pellow & Co

Project Overview:We are a handmade bath and body brand looking for an experienced packaging/label designer to create a cohesive label system for our products.

Our brand style is playful, clean, modern, bold, and slightly magical.

Scope of Work:
1. Label Template SystemDesign cohesive, print-ready templates for:
Bar soap wraps
Jar labels (scrubs, salts, creams)
Bottle labels (sprays, oils)
Small product tags
Generic shopping bag labels and stickers for shipped items.

Templates must be editable (preferably Canva-compatible) so we can update scents and product names.

Deliverables:
Print-ready files (PDF + source files)
Editable templates
Font and color specs

Ideal Candidate:
Experience with packaging/label design
Familiar with print requirements
Able to design scalable template systems
Strong portfolio of product branding work

To Apply, Please Include:

Portfolio (packaging examples preferred)
Estimated timeline
Pricing for full project
Confirmation you can provide Canva-editable files

We are looking for someone who can help create a polished, cohesive visual system for a growing product brand.

Target Market(s)

All ages, modern urban families, wide range demographics and ethnicities.

Industry/Entity Type

Soap, lotions, cosmetics

Font styles to use
Serif

Colors
FFC000
F8CF3A
FAE287
FDF2CF
FEFAEE
F0912C
F2A743
F7CA91
FBE8D2
FDF5EE
E54698
E96AAD
F1A4CE
F9D9EA
FCEFF6

Requirements
Must have
• Somewhat similar concept to example photos given, but would like you to bring your own creative ideas based on it.
Nice to have
• Water elements (flowing movement), mystical elements
Should not have
• Apothecary, farmhouse or floral style, bubbles, elegant or ornate script font

```html
<!DOCTYPE html>
<html lang="en">
<head>
<meta charset="utf-8">
<title>Pellow &amp; Co. — Soap Wrap Labels</title>
<link rel="stylesheet" href="https://fonts.googleapis.com/css2?family=Caveat+Brush&family=Fraunces:opsz,wght@9..144,400;9..144,700&family=Libre+Caslon+Text&display=swap">
<style>
  :root {
    --canvas: #f6f4f7;
    --ink: #111111;
    --wrap-green: #b8dea3;
    --wrap-pink: #f2a9d5;
  }
  * { box-sizing: border-box; margin: 0; padding: 0; }
  html, body {
    width: 1200px;
    height: 800px;
    overflow: hidden;
    background: var(--canvas);
  }
  .label-sheet {
    position: relative;
    width: 1200px;
    height: 800px;
  }
  .soap-wrap {
    position: absolute;
    top: 278px;
    width: 522px;
    height: 246px;
    color: var(--ink);
  }
  .soap-wrap--citrus { left: 64px; background: var(--wrap-green); }
  .soap-wrap--rose { left: 612px; background: var(--wrap-pink); }

  .wrap-side {
    position: absolute;
    top: 38px;
    font-family: "Libre Caslon Text", Georgia, serif;
    font-size: 15px;
    line-height: 0.98;
    text-align: center;
    letter-spacing: 0.01em;
  }
  .wrap-side--left { left: 36px; }
  .wrap-side--right { right: 58px; }

  .brand-name {
    position: absolute;
    top: 30px;
    left: 0;
    right: 0;
    text-align: center;
    font-family: "Fraunces", Georgia, serif;
    font-weight: 700;
    font-size: 42px;
    letter-spacing: -0.035em;
    line-height: 1;
  }

  .product-name {
    position: absolute;
    top: 92px;
    left: 0;
    right: 0;
    text-align: center;
    font-family: "Caveat Brush", "Comic Sans MS", cursive;
    font-size: 84px;
    line-height: 1;
    white-space: nowrap;
  }
  .product-name .joiner {
    font-size: 38px;
    display: inline-block;
    transform: translateY(16px);
    margin: 0 -6px 0 -14px;
  }
  .product-name .word-gap { display: inline-block; width: 26px; }

  .tagline {
    position: absolute;
    bottom: 22px;
    left: 0;
    right: 0;
    text-align: center;
    font-family: "Libre Caslon Text", Georgia, serif;
    font-size: 13px;
    letter-spacing: 0.5em;
    padding-left: 0.5em;
  }
</style>
</head>
<body>
<main class="label-sheet">
  <section class="soap-wrap soap-wrap--citrus">
    <p class="wrap-side wrap-side--left">HAND &amp;<br>HEART</p>
    <h2 class="brand-name">Pellow &amp; Co.</h2>
    <p class="wrap-side wrap-side--right">EST.<br>2020</p>
    <h1 class="product-name">Citrus<span class="joiner">and</span> Ginger</h1>
    <p class="tagline">SMALL BATCH ARTISAN SOAP</p>
  </section>

  <section class="soap-wrap soap-wrap--rose">
    <p class="wrap-side wrap-side--left">HAND &amp;<br>HEART</p>
    <h2 class="brand-name">Pellow &amp; Co.</h2>
    <p class="wrap-side wrap-side--right">EST.<br>2020</p>
    <h1 class="product-name">Rose<span class="word-gap"></span>Clay</h1>
    <p class="tagline">SMALL BATCH ARTISAN SOAP</p>
  </section>
</main>
</body>
</html>
```